A start up special flyer design!

Hi All - Have updated the attachment content - This is the info required for the designs.
I need a catchy flyer to send out to a few areas to advertise the start of my plumbing business!
The flyer will contain an offer for customers, which will need to have some key details on it. See attached. Feel free to fit these criteria into the flyer given your knowledge on design and messaging principles. Key thing to get across to customers is the discount and special offer, and that it is a start up offer.
I have a logo that needs to be on the flyer as well - let me know what format you require and I will send through to you.
The color scheme needs to be blue / grey / black / white.
Let me know if you have any questions.
I

```html
<!DOCTYPE html>
<html lang="en">
<head>
<meta charset="utf-8">
<title>Ricky Flow Plumbing – Start-up Offer Flyer</title>
<link href="https://fonts.googleapis.com/css2?family=Oswald:wght@400;500&family=Roboto:wght@500;700&family=Josefin+Sans:wght@700&family=Special+Elite&display=swap" rel="stylesheet">
<style>
  :root{
    --page-bg:#d3d3d3;
    --blue:#0f5df0;
    --blue-deep:#0a3fc0;
    --blue-bright:#1a7cf5;
    --navy:#0b2aa8;
    --black-band:#1a1b21;
    --grey-panel:#c9cbd0;
    --yellow:#f6e51d;
    --white:#ffffff;
    --ink:#17171a;
  }
  *{box-sizing:border-box;margin:0;padding:0}
  html,body{width:1200px;height:1200px;overflow:hidden;background:var(--page-bg)}
  .flyer{position:absolute;left:212px;top:52px;width:775px;height:1096px;background:var(--grey-panel);overflow:hidden;box-shadow:0 8px 24px rgba(0,0,0,.35)}

  /* header */
  .header{position:absolute;left:0;top:0;width:775px;height:282px;background:radial-gradient(ellipse at 60% 40%,#5c5c5c,#2f2f2f)}
  .header-photo{position:absolute;inset:0;background:linear-gradient(180deg,rgba(40,80,200,.18) 0%,rgba(0,0,0,0) 60%)}
  .offer-note{position:absolute;left:217px;top:62px;width:86px;height:86px;background:var(--yellow);transform:rotate(18deg);display:flex;align-items:center;justify-content:center;box-shadow:2px 3px 6px rgba(0,0,0,.35)}
  .offer-note span{font-family:"Special Elite",serif;font-size:21px;color:#3a3000;transform:rotate(-18deg)}
  .nameplate{position:absolute;left:116px;top:176px;width:652px;height:76px;background:linear-gradient(180deg,#b8b8b8,#959595);display:flex;align-items:center;justify-content:center;box-shadow:0 3px 8px rgba(0,0,0,.45)}
  .nameplate h1{font-family:"Josefin Sans",sans-serif;font-weight:700;font-size:40px;letter-spacing:1px;color:var(--ink);padding-top:6px}

  /* offer band */
  .offer-band{position:absolute;left:0;top:282px;width:775px;height:274px;background:linear-gradient(135deg,var(--blue-deep) 0%,var(--blue) 55%,var(--blue-bright) 100%)}
  .services-band{position:absolute;left:0;top:556px;width:775px;height:232px;background:var(--black-band)}
  .tradesperson{position:absolute;left:8px;top:286px;width:200px;height:500px;background:linear-gradient(180deg,#1b2a5a 0%,#1d2440 55%,#2b3e6e 100%);border-radius:90px 90px 0 0}

  .list{position:absolute;left:213px;list-style:none}
  .list li{display:flex;align-items:center;font-family:"Oswald",sans-serif;color:var(--white)}
  .list svg{flex:none;width:36px;height:36px;margin-right:21px}
  .offer-list{top:302px}
  .offer-list li{font-size:22px;height:74px}
  .services-list{top:574px}
  .services-list li{font-size:22px;height:50px}

  /* contact */
  .appointment{position:absolute;left:46px;top:788px;width:680px;height:92px;background:linear-gradient(90deg,#a9acb4,#eceef2 60%,#d6d8dc);clip-path:polygon(0 0,100% 0,93% 100%,0 100%);padding:16px 0 0 68px}
  .appointment p{font-family:"Roboto",sans-serif;font-weight:500;font-size:23px;line-height:29px;color:var(--ink)}
  .appointment strong{color:var(--navy);font-weight:500}
  .ribbon{position:absolute;left:13px;top:880px;width:749px;height:132px;background:linear-gradient(90deg,var(--navy) 0%,var(--blue) 55%,var(--blue-bright) 100%);overflow:hidden}
  .ribbon-slash{position:absolute;left:366px;top:0;width:34px;height:132px;background:var(--white);transform:skewX(24deg)}
  .phone{position:absolute;left:14px;top:22px;font-family:"Oswald",sans-serif;font-weight:500;font-size:62px;line-height:88px;color:var(--white);letter-spacing:-1px;white-space:nowrap}
  .contact-lines{position:absolute;left:434px;top:34px;list-style:none}
  .contact-lines li{display:flex;align-items:center;height:37px;font-family:"Roboto",sans-serif;font-weight:700;font-size:18px;color:var(--white);white-space:nowrap}
  .contact-lines svg{width:20px;height:20px;margin-right:14px;flex:none}
  .fineprint{position:absolute;left:46px;top:1012px;width:680px;height:66px;background:linear-gradient(90deg,#b1b4bb,#f1f2f4);padding:12px 0 0 44px;font-family:"Oswald",sans-serif;font-size:12px;color:#2b2b2e;line-height:16px}
  .fineprint .right{position:absolute;left:430px;top:12px}
</style>
</head>
<body>
<main class="flyer">
  <section class="header">
    <div class="header-photo" role="img" aria-label="Photo of blue-painted pipe valves and caps on a dark textured wall"></div>
    <div class="offer-note"><span>OFFER</span></div>
    <div class="nameplate"><h1>RICKY FLOW PLUMBING</h1></div>
  </section>

  <section class="offer-band"></section>
  <section class="services-band"></section>
  <div class="tradesperson" role="img" aria-label="Photo of a smiling plumber with folded arms wearing a navy polo and tool belt"></div>

  <ul class="list offer-list">
    <li><svg viewBox="0 0 36 36"><rect x="2" y="8" width="24" height="24" fill="none" stroke="#f6e51d" stroke-width="3"/><path d="M7 19l7 7L33 4" fill="none" stroke="#f6e51d" stroke-width="4"/></svg>15% off your overall bill *</li>
    <li><svg viewBox="0 0 36 36"><rect x="2" y="8" width="24" height="24" fill="none" stroke="#f6e51d" stroke-width="3"/><path d="M7 19l7 7L33 4" fill="none" stroke="#f6e51d" stroke-width="4"/></svg>No GST payable, saving you additional 10% on your bill ^</li>
    <li><svg viewBox="0 0 36 36"><rect x="2" y="8" width="24" height="24" fill="none" stroke="#f6e51d" stroke-width="3"/><path d="M7 19l7 7L33 4" fill="none" stroke="#f6e51d" stroke-width="4"/></svg>Plus, a free hot water health check and replacement quote ~</li>
  </ul>

  <ul class="list services-list">
    <li><svg viewBox="0 0 36 36" fill="none" stroke="#f6e51d" stroke-width="2"><path d="M12 6h12M18 6v6M6 14h24v6H20v4h-4v-4H6z"/><path d="M18 28c0 2 2 3 2 3"/></svg>All plumbing, draining, and gasfitting works</li>
    <li><svg viewBox="0 0 36 36" fill="none" stroke="#f6e51d" stroke-width="2"><path d="M5 20l8 10L32 5"/></svg>“Quality work at a decent price”</li>
    <li><svg viewBox="0 0 36 36" fill="none" stroke="#f6e51d" stroke-width="2"><path d="M6 6l24 24M30 6L6 30"/><circle cx="8" cy="8" r="3"/><circle cx="28" cy="28" r="3"/></svg>“Local plumber”</li>
  </ul>

  <div class="appointment">
    <p>To make an <strong>APPOINTMENT</strong>, call or email Ricky,<br>or alternatively make a booking directly on the website.</p>
  </div>

  <div class="ribbon">
    <div class="ribbon-slash"></div>
    <div class="phone">0400 555 218</div>
    <ul class="contact-lines">
      <li><svg viewBox="0 0 20 20" fill="none" stroke="#fff" stroke-width="1.6"><rect x="1" y="4" width="18" height="12"/><path d="M1 4l9 7 9-7"/></svg>ricky@rickyflowplumbing.com</li>
      <li><svg viewBox="0 0 20 20" fill="none" stroke="#fff" stroke-width="1.4"><circle cx="10" cy="10" r="8.5"/><ellipse cx="10" cy="10" rx="3.5" ry="8.5"/><path d="M1.5 10h17M3 5.5h14M3 14.5h14"/></svg>www.rickyflowplumbing.com</li>
    </ul>
  </div>

  <div class="fineprint">
    * Offer valid between 15 August 2016 to 15 October 2016.<br>
    &nbsp;^ Valid until 30 September 2016.
    <span class="right">~ Quote valid for 12 months from the quote date.</span>
  </div>
</main>
</body>
</html>
```